Business Card + Stationary
TBV Financial Group
Professional
Dale Morrow
Business Development Manager
2718 SW 9th Ave. Suite 1146
Renton, WA 98059 Toll Free
dale@tbvfinancialgroup.example
www.tbvfinancialgroup.example
want to modernize & update website and design.
Feel free to update/ change TBV logo as you see fit.
Logo
More of a high res logo
eps logo
TBV Background (not sure if the quality is good enough though)

```html
<!DOCTYPE html>
<html lang="en">
<head>
<meta charset="utf-8">
<title>TBV Financial Group – Stationery</title>
<link href="https://fonts.googleapis.com/css2?family=Tinos:wght@400;700&display=swap" rel="stylesheet">
<style>
  :root {
    --navy: #114182;
    --ink: #1b1b1b;
    --paper: #ffffff;
    --backdrop: #eceef1;
    --muted: #555b66;
    --faint: #e3e7ee;
    --pale-text: #cdd8ea;
  }
  * { box-sizing: border-box; margin: 0; padding: 0; }
  html, body { width: 1200px; height: 936px; overflow: hidden; }
  body {
    background: var(--backdrop);
    font-family: "Tinos", "Times New Roman", serif;
    color: var(--ink);
    position: relative;
  }
  .sheet { position: absolute; background: var(--paper); overflow: hidden; }
  .wave { position: absolute; left: 0; bottom: 0; width: 100%; }

  /* logo lockup */
  .brand { display: flex; align-items: center; gap: 8px; font-weight: 700; color: var(--ink); }
  .brand-mark { background: var(--navy); flex: none; }
  .brand-text { display: flex; flex-direction: column; line-height: 1; }
  .brand-name { letter-spacing: 0.02em; }
  .brand-sub { letter-spacing: 0.04em; margin-top: 3px; white-space: nowrap; }
  .brand--light { color: var(--paper); }
  .brand--light .brand-mark { background: var(--paper); }

  .contact { font-size: 6.5px; line-height: 1.5; color: var(--muted); white-space: nowrap; }

  /* letterhead */
  .letterhead { left: 183px; top: 68px; width: 388px; height: 543px; }
  .letterhead .brand { position: absolute; left: 25px; top: 28px; }
  .letterhead .brand-mark { width: 22px; height: 22px; }
  .letterhead .brand-name { font-size: 28px; }
  .letterhead .brand-sub { font-size: 6px; }
  .letterhead .contact { position: absolute; left: 262px; top: 14px; }
  .letterhead .watermark {
    position: absolute; left: 0; right: 0; top: 255px; text-align: center;
    font-weight: 700; font-size: 42px; color: var(--faint); letter-spacing: 0.04em;
  }

  /* folder */
  .folder { left: 634px; top: 38px; width: 396px; height: 576px; }
  .folder .brand { position: absolute; left: 95px; top: 255px; gap: 12px; }
  .folder .brand-mark { width: 44px; height: 44px; }
  .folder .brand-name { font-size: 58px; }
  .folder .brand-sub { font-size: 12px; margin-top: 5px; }

  /* business cards */
  .card-front { left: 43px; top: 655px; width: 178px; height: 101px; }
  .card-front .brand { position: absolute; right: 10px; top: 8px; gap: 4px; }
  .card-front .brand-mark { width: 9px; height: 9px; }
  .card-front .brand-name { font-size: 13px; }
  .card-front .brand-sub { font-size: 3.5px; margin-top: 1px; }
  .card-front .person { position: absolute; left: 10px; top: 30px; font-size: 5px; line-height: 1.45; color: var(--muted); }
  .card-front .person strong { color: var(--ink); font-size: 5.5px; }
  .card-front .contact { position: absolute; left: 88px; top: 30px; font-size: 4.2px; }

  .card-back { left: 43px; top: 774px; width: 178px; height: 104px; background: var(--navy); }
  .card-back .brand { position: absolute; left: 50%; top: 30px; transform: translateX(-50%); gap: 5px; }
  .card-back .brand-mark { width: 12px; height: 12px; }
  .card-back .brand-name { font-size: 18px; }
  .card-back .web {
    position: absolute; left: 10px; right: 10px; bottom: 9px;
    font-size: 4.8px; color: var(--pale-text); letter-spacing: 0.05em; white-space: nowrap;
  }

  /* envelopes */
  .envelope-front { left: 264px; top: 672px; width: 434px; height: 203px; }
  .envelope-front .brand { position: absolute; left: 16px; top: 22px; gap: 6px; }
  .envelope-front .brand-mark { width: 16px; height: 16px; }
  .envelope-front .brand-name { font-size: 24px; }
  .envelope-front .brand-sub { font-size: 5px; }
  .envelope-front .contact { position: absolute; left: 16px; top: 88px; font-size: 5px; }

  .envelope-back { left: 738px; top: 672px; width: 419px; height: 203px; }
  .envelope-back .flap { position: absolute; left: 0; top: 0; width: 100%; height: 92px; }
  .envelope-back .web {
    position: absolute; left: 0; right: 0; top: 8px; text-align: center;
    font-size: 11px; letter-spacing: 0.16em; color: var(--paper);
  }
</style>
</head>
<body>

<section class="sheet letterhead">
  <div class="brand">
    <span class="brand-mark"></span>
    <span class="brand-text"><span class="brand-name">TBV</span><span class="brand-sub">FINANCIAL GROUP, INC.</span></span>
  </div>
  <div class="contact">
    2718 SW 9th Ave. Suite 1146<br>
    Cedarford, WA 98000<br>
    Phone: (425) 555-0147<br>
    dale@tbvfinancialgroup.example<br>
    www.tbvfinancialgroup.example
  </div>
  <div class="watermark">TBV</div>
  <svg class="wave" viewBox="0 0 388 140" height="140" preserveAspectRatio="none" aria-hidden="true">
    <path d="M0,100 C120,128 260,112 388,38 L388,140 L0,140 Z" fill="var(--navy)"/>
    <path d="M0,86 C130,116 262,98 388,22" fill="none" stroke="#111" stroke-width="2"/>
  </svg>
</section>

<section class="sheet folder">
  <div class="brand">
    <span class="brand-mark"></span>
    <span class="brand-text"><span class="brand-name">TBV</span><span class="brand-sub">FINANCIAL GROUP, INC.</span></span>
  </div>
  <svg class="wave" viewBox="0 0 396 180" height="180" preserveAspectRatio="none" aria-hidden="true">
    <path d="M0,150 C110,150 170,50 396,34 L396,180 L0,180 Z" fill="var(--navy)"/>
    <path d="M0,138 C110,140 170,40 396,22" fill="none" stroke="#111" stroke-width="2.5"/>
  </svg>
</section>

<section class="sheet card-front">
  <div class="brand">
    <span class="brand-mark"></span>
    <span class="brand-text"><span class="brand-name">TBV</span><span class="brand-sub">FINANCIAL GROUP, INC.</span></span>
  </div>
  <div class="person"><strong>Dale Morrow</strong><br>Business Development<br>Manager</div>
  <div class="contact">
    2718 SW 9th Ave. Suite 1146<br>
    Cedarford, WA 98000<br>
    dale@tbvfinancialgroup.example<br>
    www.tbvfinancialgroup.example
  </div>
  <svg class="wave" viewBox="0 0 178 36" height="36" preserveAspectRatio="none" aria-hidden="true">
    <path d="M0,24 C60,34 120,28 178,6 L178,36 L0,36 Z" fill="var(--navy)"/>
    <path d="M0,19 C60,30 120,22 178,1" fill="none" stroke="#111" stroke-width="1"/>
  </svg>
</section>

<section class="sheet card-back">
  <div class="brand brand--light">
    <span class="brand-mark"></span>
    <span class="brand-text"><span class="brand-name">TBV</span></span>
  </div>
  <div class="web">www.tbvfinancialgroup.example</div>
</section>

<section class="sheet envelope-front">
  <div class="brand">
    <span class="brand-mark"></span>
    <span class="brand-text"><span class="brand-name">TBV</span><span class="brand-sub">FINANCIAL GROUP, INC.</span></span>
  </div>
  <div class="contact">
    2718 SW 9th Ave. Suite 1146<br>
    Cedarford, WA 98000
  </div>
  <svg class="wave" viewBox="0 0 434 80" height="80" preserveAspectRatio="none" aria-hidden="true">
    <path d="M0,72 C150,74 280,60 434,8 L434,80 L0,80 Z" fill="var(--navy)"/>
    <path d="M0,64 C150,68 280,50 434,0" fill="none" stroke="#111" stroke-width="1.5"/>
  </svg>
</section>

<section class="sheet envelope-back">
  <svg class="flap" viewBox="0 0 419 92" preserveAspectRatio="none" aria-hidden="true">
    <path d="M0,0 L419,0 L419,30 L209.5,92 L0,30 Z" fill="var(--navy)"/>
  </svg>
  <div class="web">www.TbvFinancialGroup.example</div>
</section>

</body>
</html>
```